Kerris Odlen Letter Head

log and letter head

would like a modern feminine approch, please see attached the back of my business card

Kerris Odlen Consulting

ABN 81 540 263 918

Address19a Brood Street Corrin Bay 5082 South Australia

Business

```html
<!DOCTYPE html>
<html lang="en">
<head>
<meta charset="utf-8">
<title>Kerris Odlen Consulting – Letterhead</title>
<link rel="stylesheet" href="https://fonts.googleapis.com/css2?family=Questrial&display=swap">
<style>
  :root {
    --backdrop: #ececec;
    --paper: #fafafa;
    --brand-red: #d9534a;
    --swoosh-grey: #a8a8a8;
    --ink: #4a4a4a;
  }
  * { margin: 0; padding: 0; box-sizing: border-box; }
  html, body {
    width: 1200px;
    height: 936px;
    overflow: hidden;
    background: var(--backdrop);
  }
  .letterhead {
    position: absolute;
    left: 289px;
    top: 28px;
    width: 622px;
    height: 880px;
    background: var(--paper);
    box-shadow: 0 4px 18px rgba(0, 0, 0, 0.12);
    overflow: hidden;
    font-family: "Questrial", "Century Gothic", sans-serif;
  }
  .swoosh {
    position: absolute;
    left: 0;
    top: 0;
    width: 622px;
    height: 880px;
  }
  .swoosh-top { fill: var(--swoosh-grey); }
  .swoosh-bottom { fill: var(--brand-red); }
  .brand {
    position: absolute;
    left: 70px;
    top: 96px;
    color: var(--brand-red);
    text-align: center;
  }
  .brand-name {
    display: block;
    font-size: 30px;
    line-height: 1;
    letter-spacing: 0.5px;
  }
  .brand-tagline {
    display: block;
    margin-top: 6px;
    font-size: 8px;
    letter-spacing: 6px;
    text-transform: uppercase;
  }
  .footer-address {
    position: absolute;
    right: 24px;
    bottom: 104px;
    font-size: 8.5px;
    color: var(--ink);
    letter-spacing: 0.2px;
    white-space: nowrap;
  }
</style>
</head>
<body>
  <main class="letterhead">
    <svg class="swoosh" viewBox="0 0 622 880" aria-hidden="true">
      <path class="swoosh-top" d="M0,0 L560,0 Q300,14 0,96 Z"/>
      <path class="swoosh-bottom" d="M622,880 L170,880 Q440,846 622,762 Z"/>
    </svg>

    <header class="brand">
      <span class="brand-name">Kerris Odlen</span>
      <span class="brand-tagline">Consulting</span>
    </header>

    <footer class="footer-address">
      27c Tallow Lane Corrin Bay 5082 South Australia · ABN 81 540 263 918
    </footer>
  </main>
</body>
</html>
```